Brovanta MRI

In addition to basic information on name card, please also add QR code.

Target Market(s)

Doctors, hospitals and patients

Industry/Entity Type

Diagnostic MRI imaging center

Contact Information for Business Card

Name, address, email , phone number, fax number, website , cell phone number, title, business scope,

Font styles to use
Sans Serif

Colors
FFC000
F8CF3A
FAE287
FDF2CF
FEFAEE

Requirements
Must have
• My logo
Nice to have
• Introduction of my business scope

```html
<!DOCTYPE html>
<html lang="en">
<head>
<meta charset="utf-8">
<title>Brovanta MRI – Business Card</title>
<link href="https://fonts.googleapis.com/css2?family=Lato:wght@400;700;900&display=swap" rel="stylesheet">
<style>
  :root {
    --backdrop: #2b2b2b;
    --card-black: #141414;
    --brand-orange: #f7941d;
    --brand-grey: #a3a3a6;
    --ink: #1a1a1a;
  }
  * { margin: 0; padding: 0; box-sizing: border-box; }
  html, body { width: 1200px; height: 875px; overflow: hidden; }
  body {
    background: var(--backdrop);
    font-family: "Lato", sans-serif;
    display: flex;
    flex-direction: column;
    align-items: center;
    justify-content: center;
    gap: 60px;
  }
  .card {
    width: 640px;
    height: 366px;
    border-radius: 22px;
    background: var(--card-black);
    position: relative;
    overflow: hidden;
    box-shadow: 0 12px 30px rgba(0,0,0,0.45);
  }
  .brand {
    display: flex;
    align-items: center;
    gap: 16px;
    color: var(--brand-grey);
    font-weight: 400;
    letter-spacing: 2px;
    white-space: nowrap;
  }
  .brand-dot {
    border-radius: 50%;
    background: var(--brand-orange);
    flex: none;
  }
  .card-front { display: flex; align-items: center; justify-content: center; }
  .card-front .brand { font-size: 56px; }
  .card-front .brand-dot { width: 48px; height: 48px; }

  .card-back .contact-panel {
    position: absolute;
    left: 0; top: 0; bottom: 0;
    width: 360px;
    background: var(--brand-orange);
    border-radius: 22px 0 0 22px;
    clip-path: polygon(0 0, 84% 0, 100% 100%, 0 100%);
    padding: 48px 0 0 40px;
    color: var(--ink);
  }
  .person-name { font-size: 27px; font-weight: 900; letter-spacing: 0.5px; }
  .person-title { font-size: 19px; margin-top: 2px; }
  .contact-list { list-style: none; margin-top: 26px; font-size: 17px; line-height: 1.35; }
  .contact-list li { display: flex; align-items: flex-start; gap: 12px; }
  .contact-list svg { width: 14px; height: 14px; flex: none; margin-top: 4px; fill: var(--ink); }
  .contact-list .address { margin-bottom: 10px; }
  .card-back .brand-area {
    position: absolute;
    left: 370px; right: 0; top: 0;
    height: 250px;
    display: flex;
    align-items: center;
    justify-content: center;
  }
  .card-back .brand { font-size: 26px; gap: 10px; letter-spacing: 1.5px; }
  .card-back .brand-dot { width: 22px; height: 22px; }
</style>
</head>
<body>
  <section class="card card-front" aria-label="Card front">
    <div class="brand"><span class="brand-dot"></span>Brovanta MRI</div>
  </section>

  <section class="card card-back" aria-label="Card back">
    <div class="contact-panel">
      <h1 class="person-name">DANIEL HARPER</h1>
      <p class="person-title">Founder &amp; CEO</p>
      <ul class="contact-list">
        <li class="address">
          <svg viewBox="0 0 16 16"><path d="M8 0a5.5 5.5 0 0 0-5.5 5.5C2.5 10 8 16 8 16s5.5-6 5.5-10.5A5.5 5.5 0 0 0 8 0zm0 8a2.5 2.5 0 1 1 0-5 2.5 2.5 0 0 1 0 5z"/></svg>
          <span>Your Address, City<br>State, Zip 1235</span>
        </li>
        <li>
          <svg viewBox="0 0 16 16"><path d="M3.6 1l2.6 2.6-1.5 2.2a10 10 0 0 0 5.5 5.5l2.2-1.5L15 12.4 13 15C6 14 2 10 1 3z"/></svg>
          <span>(123) 456-7890</span>
        </li>
        <li>
          <svg viewBox="0 0 16 16"><path d="M4 0h8a1 1 0 0 1 1 1v14a1 1 0 0 1-1 1H4a1 1 0 0 1-1-1V1a1 1 0 0 1 1-1zm1 2v10h6V2zm3 11a1 1 0 1 0 0 2 1 1 0 0 0 0-2z"/></svg>
          <span>(123) 456-7890</span>
        </li>
        <li>
          <svg viewBox="0 0 16 16"><path d="M4 0h8v4H4zM1 5h14v7h-3v4H4v-4H1zm5 6v3h4v-3z"/></svg>
          <span>(123) 456-7890</span>
        </li>
        <li>
          <svg viewBox="0 0 16 16"><path d="M0 3h16v1L8 9 0 4zm0 3l8 5 8-5v7H0z"/></svg>
          <span>info@yourwebsite.com</span>
        </li>
        <li>
          <svg viewBox="0 0 16 16"><path d="M8 0a8 8 0 1 0 0 16A8 8 0 0 0 8 0zm0 2a6 6 0 0 1 5.7 4H10V4H6v3H3v3h5v4a6 6 0 0 1 0-12z"/></svg>
          <span>yourwebsite.com</span>
        </li>
      </ul>
    </div>
    <div class="brand-area">
      <div class="brand"><span class="brand-dot"></span>Brovanta MRI</div>
    </div>
  </section>
</body>
</html>
```